Business Card Design

We are an IT staffing and consulting company providing IT solutions and resources to our clients.

Industry/Entity Type

Business

Contact Information for Business Card

Ramesh Tulavarthi
Vice President

BrightNode Inc
48215 Harrowmere Court Square, suite 700
Ashburn, VA 20147
Direct: 571-555-0193
Mobile: 571-555-0147
Email: Ramesh@brightnodeinc.com
Fax: 703-555-0162
www.brightnodeinc.com

```html
<!DOCTYPE html>
<html lang="en">
<head>
<meta charset="utf-8">
<title>BrightNode Inc — Business Card</title>
<link href="https://fonts.googleapis.com/css2?family=Open+Sans:wght@400;600&display=swap" rel="stylesheet">
<style>
  :root {
    --backdrop: #b9b9b7;
    --card-black: #0c0c0c;
    --card-black-soft: #181818;
    --accent-red: #d3203c;
    --text-white: #f4f4f4;
    --rule-grey: #3a3a3a;
  }
  * { margin: 0; padding: 0; box-sizing: border-box; }
  html, body {
    width: 1200px;
    height: 900px;
    overflow: hidden;
    background: var(--backdrop);
    font-family: "Open Sans", Arial, sans-serif;
  }
  .canvas {
    position: relative;
    width: 1200px;
    height: 900px;
  }
  .card {
    position: absolute;
    left: 320px;
    width: 560px;
    height: 320px;
    background: linear-gradient(135deg, var(--card-black-soft) 0%, var(--card-black) 60%);
    box-shadow: 0 6px 18px rgba(0,0,0,0.25);
    overflow: hidden;
  }
  .card--back { top: 100px; }
  .card--front { top: 480px; }

  .back-name {
    position: absolute;
    left: 0; right: 0;
    top: 138px;
    text-align: center;
    color: var(--accent-red);
    font-weight: 600;
    font-size: 34px;
    letter-spacing: 0.5px;
  }

  .holder {
    position: absolute;
    left: 40px;
    top: 72px;
  }
  .holder-name {
    color: var(--text-white);
    font-weight: 600;
    font-size: 22px;
    line-height: 1.2;
  }
  .holder-title {
    color: var(--accent-red);
    font-weight: 400;
    font-size: 15px;
    line-height: 1.3;
  }

  .company-name {
    position: absolute;
    right: 30px;
    top: 60px;
    color: var(--text-white);
    font-weight: 600;
    font-size: 34px;
    letter-spacing: 1px;
  }

  .divider {
    position: absolute;
    left: 220px;
    right: 30px;
    top: 128px;
    height: 1px;
    background: var(--rule-grey);
  }

  .contact-list {
    position: absolute;
    right: 30px;
    top: 140px;
    list-style: none;
  }
  .contact-item {
    display: flex;
    align-items: center;
    justify-content: flex-end;
    gap: 12px;
    color: var(--text-white);
    font-size: 14px;
    line-height: 23px;
    white-space: nowrap;
  }
  .contact-label {
    color: var(--accent-red);
    margin-right: 4px;
  }
  .contact-icon {
    width: 11px;
    height: 11px;
    flex: none;
  }
</style>
</head>
<body>
<main class="canvas">

  <section class="card card--back" aria-label="Business card, back">
    <p class="back-name">BrightNode</p>
  </section>

  <section class="card card--front" aria-label="Business card, front">
    <div class="holder">
      <p class="holder-name">Ramesh Tulavarthi</p>
      <p class="holder-title">Vice President</p>
    </div>

    <p class="company-name">BrightNode</p>

    <div class="divider"></div>

    <ul class="contact-list">
      <li class="contact-item">
        <span><span class="contact-label">Direct:</span>571-555-0193</span>
        <svg class="contact-icon" viewBox="0 0 12 12" aria-hidden="true">
          <path d="M1 4 Q6 0 11 4 L9.5 5.5 L8 4.3 L4 4.3 L2.5 5.5 Z" fill="var(--accent-red)"/>
          <rect x="2.5" y="6" width="7" height="5" rx="1" fill="var(--accent-red)"/>
        </svg>
      </li>
      <li class="contact-item">
        <span><span class="contact-label">Mobile:</span>571-555-0147</span>
        <svg class="contact-icon" viewBox="0 0 12 12" aria-hidden="true">
          <rect x="3" y="0.5" width="6" height="11" rx="1.2" fill="none" stroke="var(--accent-red)" stroke-width="1.3"/>
          <circle cx="6" cy="9.3" r="0.8" fill="var(--accent-red)"/>
        </svg>
      </li>
      <li class="contact-item">
        <span><span class="contact-label">Fax:</span>703-555-0162</span>
        <svg class="contact-icon" viewBox="0 0 12 12" aria-hidden="true">
          <rect x="3" y="0.5" width="6" height="4" fill="none" stroke="var(--accent-red)" stroke-width="1.2"/>
          <rect x="0.5" y="4.5" width="11" height="5" rx="1" fill="var(--accent-red)"/>
          <rect x="3" y="8" width="6" height="3.5" fill="var(--accent-red)"/>
        </svg>
      </li>
      <li class="contact-item">
        <span>Ramesh@brightnodeinc.com</span>
        <svg class="contact-icon" viewBox="0 0 12 12" aria-hidden="true">
          <rect x="0.5" y="2.5" width="11" height="7.5" fill="var(--accent-red)"/>
          <path d="M0.5 2.5 L6 7 L11.5 2.5" fill="none" stroke="var(--card-black)" stroke-width="1"/>
        </svg>
      </li>
      <li class="contact-item">
        <span>www.brightnodeinc.com</span>
        <svg class="contact-icon" viewBox="0 0 12 12" aria-hidden="true">
          <path d="M5 7 L7 5 M4.5 5.5 L2.5 7.5 a1.8 1.8 0 0 0 2.5 2.5 L7 8 M7.5 6.5 L9.5 4.5 a1.8 1.8 0 0 0 -2.5 -2.5 L5 4"
                fill="none" stroke="var(--accent-red)" stroke-width="1.3" stroke-linecap="round"/>
        </svg>
      </li>
      <li class="contact-item">
        <span>48215 Harrowmere Court Square, suite 700, Ashburn, VA 20147</span>
        <svg class="contact-icon" viewBox="0 0 12 12" aria-hidden="true">
          <path d="M6 11.5 L2.6 6.2 A4 4 0 1 1 9.4 6.2 Z" fill="var(--accent-red)"/>
          <circle cx="6" cy="4.2" r="1.4" fill="var(--card-black)"/>
        </svg>
      </li>
    </ul>
  </section>

</main>
</body>
</html>
```